依頼概要
■依頼の目的/概要
ベーカリーを運営しております。
新商品(食パン)のPOPを作成して頂きたいです。

■依頼詳細
通常より高単価な商品のため、画像や価格よりも、セールスコピーやキャプションを重視した見せ方にしていただきたいです。
食パンのイメージ画像を2つ添付しますが、どちらかをお使いいただければ。

■重視する点
過去・現在までにデザインの経験のある方を希望致します。

その他何かご不明な点がございましたら、お気軽にご質問下さい。
よろしくお願いいたします。
■ 選んだ理由

選定理由は、パッと目に入ってきたことです。
普段あまり黒色を使用していなかったので、特にそう感じたのかもしれません。
また、依頼内容が網羅されていたことと説得力です。
最終的には、数点を選定後、社内の関係者で投票したところ1位でした。

■ 提案者全員のお礼・コメント

皆さま、このたびはたくさんのご提案をいただき、誠にありがとうございました。

こんなに素敵なご提案がたくさん来るのならと、次回の季節POP作成時の予算も確保できましたので、機会があればぜひご参画いただけたら幸いです。

個人的には、次点に選べなかったご提案の中にも気になるものがあり、別の製作物の際にお声掛けさせていただきたいデザイナーさんもおりました。
是非またピクモアを通してご連絡させていただければと存じます。

今後とも何卒よろしくお願いいたします。

```html
<!DOCTYPE html>
<html lang="ja">
<head>
<meta charset="utf-8">
<title>ルミエール 食パン POP</title>
<link rel="stylesheet" href="https://fonts.googleapis.com/css2?family=Shippori+Mincho:wght@500;700;800&family=Cormorant+Garamond:wght@500;600&display=swap">
<style>
  :root {
    --cocoa: #4a2a17;
    --cocoa-deep: #2e190c;
    --bark: #6b3f22;
    --crust: #c8935a;
    --crust-light: #e2bd88;
    --crumb: #f3e4cc;
    --cream: #fbf4e8;
    --linen: #e4cfb2;
    --gold: #c9a063;
    --ink: #3a2414;
    --paper: #ffffff;
  }
  * { margin: 0; padding: 0; box-sizing: border-box; }
  html, body { width: 865px; height: 1200px; overflow: hidden; background: var(--paper); }
  .pop {
    position: relative;
    width: 865px;
    height: 1200px;
    overflow: hidden;
    background: var(--paper);
    font-family: "Shippori Mincho", serif;
    color: var(--ink);
  }
  .bread-photo {
    position: absolute;
    left: 0; top: 0;
    width: 865px; height: 985px;
    background:
      radial-gradient(ellipse 360px 200px at 300px 640px, rgba(251,244,232,0.95), rgba(251,244,232,0) 75%),
      radial-gradient(ellipse 300px 420px at 170px 300px, rgba(226,189,136,0.9), rgba(226,189,136,0) 75%),
      radial-gradient(ellipse 420px 160px at 380px 820px, rgba(200,147,90,0.55), rgba(200,147,90,0) 75%),
      linear-gradient(160deg, var(--cocoa-deep) 0%, var(--cocoa) 16%, var(--bark) 28%, var(--crust) 40%, var(--crumb) 55%, var(--cream) 66%, var(--linen) 82%, #cfb08a 100%);
  }
  .headline {
    position: absolute;
    left: 40px; top: 22px;
    color: var(--paper);
    font-weight: 700;
    font-size: 68px;
    line-height: 1.3;
    letter-spacing: 0.03em;
    text-shadow: 0 2px 6px rgba(0,0,0,0.35);
  }
  .product {
    position: absolute;
    left: 460px; top: 335px;
    width: 385px;
    text-align: center;
    color: var(--cocoa);
  }
  .product-name {
    font-size: 74px;
    font-weight: 700;
    letter-spacing: 0.02em;
    line-height: 1.1;
  }
  .product-latin {
    font-family: "Cormorant Garamond", serif;
    font-size: 44px;
    font-weight: 500;
    letter-spacing: 0.22em;
    line-height: 1.1;
    margin-top: 4px;
  }
  .product-unit {
    font-size: 38px;
    font-weight: 700;
    line-height: 1.1;
    margin-left: -60px;
  }
  .price {
    font-family: "Cormorant Garamond", serif;
    font-size: 92px;
    font-weight: 600;
    line-height: 1;
    margin-left: 60px;
  }
  .price .yen { font-size: 48px; vertical-align: 26px; margin-right: 6px; }
  .tax { font-size: 22px; margin-left: 60px; letter-spacing: 0.1em; }
  .story {
    position: absolute;
    left: 55px; top: 1000px;
    width: 480px;
    font-size: 15px;
    font-weight: 500;
    line-height: 2.05;
    letter-spacing: 0.03em;
    color: var(--ink);
  }
  .wheat-label {
    position: absolute;
    left: 575px; top: 915px;
    width: 270px; height: 265px;
    background: var(--cocoa);
    border-radius: 14px;
    text-align: center;
    color: var(--crumb);
    padding-top: 22px;
  }
  .label-kicker { font-size: 17px; font-weight: 700; letter-spacing: 0.05em; }
  .label-grade {
    font-size: 50px; font-weight: 800; margin-top: 20px; line-height: 1; color: var(--gold);
  }
  .label-grade small { font-size: 15px; margin-left: 2px; color: var(--crumb); }
  .label-name { font-size: 30px; font-weight: 700; margin-top: 22px; }
  .label-latin {
    font-family: "Cormorant Garamond", serif;
    font-size: 22px;
    font-weight: 600;
    letter-spacing: 0.3em;
    color: var(--gold);
    margin-top: 26px;
  }
</style>
</head>
<body>
<div class="pop">
  <div class="bread-photo" role="img" aria-label="角食パンの一斤と厚切りスライスが、ストライプのクロスの上に置かれた写真"></div>

  <h1 class="headline">やっと出会えた、<br>この食感。</h1>

  <div class="product">
    <p class="product-name">ルミエール</p>
    <p class="product-latin">LUMIERE</p>
    <p class="product-unit">1斤</p>
    <p class="price"><span class="yen">¥</span>400</p>
    <p class="tax">（税込）</p>
  </div>

  <p class="story">最高級と称されるカナダ産パン用最高級小麦1CW（No.1 Canada Western Red Spring）を使用した、香り高く、雑味のない小麦の旨味が広がる食パンを作りました。食感がソフトで歯切れよく、口どけもばつぐんです。ぜひ一度お召し上がりいただき、味の違いを感じてください。</p>

  <div class="wheat-label">
    <p class="label-kicker">カナダ最高級小麦</p>
    <p class="label-grade">1CW<small>使用</small></p>
    <p class="label-name">ルミエール</p>
    <p class="label-latin">LUMIERE</p>
  </div>
</div>
</body>
</html>
```